Pruett Design & Millwork needs a web presence. Looking for a unique Design so please submit an idea.

In brief, you should know the following about me: My company was established in 2001 and had been responsible for providing reasonable CAD Design and Custom Millwork ever since. My specialty is in the area Architectural CAD Design, Fabrication of Custom Millwork and Mouldings on a partime basis. Drawings and estimates done at a very reasonable cost. I look forward to working on your next project. Thanks in Advance, Glen 
I would like one page to show thumbnails linked to some of past millwork projects and another page with thumbnails linking to some of my house designs. I assume last page will have contact information accessed from a link on home page. I already had a logo designed which I can supply you with to design home page around. As I indicated I have a regular full time job and do this for additional income and will move to full time when I have enough business.

I have attached the logo I had designed in a couple different colors. I have also uploaded some PDF's of files that I also considered before choosing the RED LOGO to give an ideas of how we could tweak the logo to better fit the website if need be. Text is wrong in those.

Thanks,
Glen

I added my logo as a PDF side there seems to be a problem with scaling loge with the other file. Hope this helps.

Glen

Evening,
I will be hosting this site on servquill. Its looks like it will get launched with wordpress?  What will be involved from getting your design up so I can upload project pictures and and text to areas you have set aside? I am also going to upload a couple jpg of a couple recent projects so you can put in so I can get a feel of what they will look like. Thanks for all your work to date! Glen

I am not seeing alot of design variations or even many designers in fact. Is there something more from me you need? Do you need me to extend deadline?

Reason: It appears that your need some more time to submit some design changes. I will choose a design next week after changes have been submitted. Thanks for your time. Glen

Reason: Designers needs a couple days to submit some last minute changes. Thanks for all your submissions! Glen

Reason: Some last minute designs that I need to look at and give feedback on. I want to thank everyone for their designs and patience. Thanks again, Glen

Evening All,

Upon discussion with a couple of the designers I want the design done in Word Press and I have increased budget the amount they said they would need to do it for. Thanks for all submissions so far but I am still looking for the special one that stands out among the rest! Glen

I will not be extending deadline and choosing designer tomorrow morning so if you have anything else to add please do so tonight. Thanks for all your submissions. Glen

Target Market(s)

Millwork projects will be generally local where as CAD Design Projects could be emailed anywhere. Probably more USA but who knows.

Industry/Entity Type

House

Font styles to use
Other font styles liked:
• Eras Medium ITC, Calibri or Designers choice.

Requirements
Must have
• Must tie in my logo on Homepage at least. Could even be somewhat transparent in background? I will let the designer work that out.
Nice to have
• Page to point to current and past Design projects on one page and millwork on another.
Should not have
• Target a large Corporate or Global environment since it is a small business right now.

```html
<!DOCTYPE html>
<html lang="en">
<head>
<meta charset="utf-8">
<title>Pruett Design &amp; Millwork – About Us</title>
<link rel="stylesheet" href="https://fonts.googleapis.com/css2?family=Open+Sans:wght@300;400;600&display=swap">
<style>
:root{
  --red:#9e1b14;
  --red-dark:#7e0f0b;
  --text:#6b6b6b;
  --ink:#222;
  --line:#d9d9d9;
  --footer:#3b3b3b;
  --footer-text:#e6e6e6;
  --muted:#9a9a9a;
}
*{box-sizing:border-box;margin:0;padding:0}
html,body{width:1100px;height:1200px;overflow:hidden}
body{background:#fff;font-family:"Open Sans",Arial,sans-serif;color:var(--text);position:relative}
.site-header{position:absolute;left:0;top:0;width:1100px;height:148px;border-bottom:1px solid #e2e2e2;box-shadow:0 2px 3px rgba(0,0,0,.06)}
.brand{position:absolute;left:70px;top:34px;display:flex;align-items:center;gap:10px}
.brand-mark{width:34px;height:34px;background:var(--red)}
.brand-name{font-weight:600;font-size:17px;line-height:20px;color:var(--red);width:130px}
.call{position:absolute;right:85px;top:36px;text-align:right}
.call-label{font-size:15px;color:#555;font-weight:400;letter-spacing:.2px}
.call-number{font-size:25px;color:var(--red);font-weight:400;line-height:30px}
.main-nav{position:absolute;right:85px;top:100px;display:flex;font-size:16px;font-weight:600;color:var(--ink)}
.main-nav a{color:inherit;text-decoration:none;padding:0 18px;border-left:1px solid #ccc;line-height:20px}
.main-nav a:first-child{border-left:0}
.main-nav a:last-child{padding-right:0}
.main-nav a.current{color:var(--red)}
.hero{position:absolute;left:0;top:149px;width:1100px;height:248px;background:linear-gradient(180deg,#dfe6ec 0%,#f2f4f5 30%,#c9cfd3 55%,#5fa6a8 72%,#6f9a3f 100%)}
.sidebar{position:absolute;left:76px;top:429px;width:226px}
.side-box{border:1px solid var(--line);margin-bottom:11px}
.side-title{height:45px;line-height:45px;padding-left:26px;color:#fff;font-size:19px;font-weight:400}
.side-title.red{background:linear-gradient(180deg,#b3231b,var(--red-dark))}
.side-title.dark{background:linear-gradient(180deg,#5a5a5a,#2e2e2e)}
.submenu{list-style:none;padding:7px 0 8px 26px}
.submenu li{width:178px;height:27px;line-height:26px;border-bottom:1px solid var(--line);font-size:13px;color:#555;padding-left:15px;position:relative}
.submenu li:last-child{border-bottom:0}
.submenu li::before{content:"";position:absolute;left:1px;top:9px;border-left:5px solid #aaa;border-top:4px solid transparent;border-bottom:4px solid transparent}
.posts{list-style:none;padding:13px 20px 37px 26px}
.posts li{font-size:11.5px;line-height:17px;color:#666;padding-left:12px;position:relative;margin-bottom:9px}
.posts li::before{content:"";position:absolute;left:0;top:6px;width:5px;height:5px;background:#aaa}
.content{position:absolute;left:330px;top:425px;width:700px}
.content h1{font-size:30px;font-weight:300;color:var(--ink);line-height:40px;margin-bottom:6px}
.content p{font-size:11.2px;line-height:20.4px;color:var(--text)}
.content p.gap{margin-top:10px}
.gallery{display:flex;gap:14px;margin:11px 0 10px 1px}
.thumb{width:276px;height:119px}
.thumb.plan{background:linear-gradient(135deg,#1e5fa8,#2f7fc9 60%,#1a4f8f)}
.thumb.night{background:linear-gradient(180deg,#3f6fa0 0%,#d89a3a 55%,#5a3a1e 100%)}
.site-footer{position:absolute;left:0;top:1073px;width:1100px;height:127px;background:var(--footer);border-top:5px solid #e8e8e8}
.footer-brand{position:absolute;left:72px;top:28px;display:flex;align-items:center;gap:8px}
.footer-brand .brand-mark{width:24px;height:24px;background:#fff}
.footer-brand .brand-name{color:#fff;font-size:13px;line-height:16px;width:90px}
.footer-nav{position:absolute;left:195px;top:30px;font-size:15px;color:var(--footer-text)}
.footer-nav span{color:#bbb;padding:0 8px}
.copyright{position:absolute;left:195px;top:56px;font-size:12.5px;color:var(--muted);font-weight:300}
.social{position:absolute;left:901px;top:36px;display:flex;gap:9px}
.social i{display:block;width:22px;height:22px;border-radius:2px}
.social .s1{background:#3b5b9b}.social .s2{background:#3fa9e0}.social .s3{background:#1f6fa7}.social .s4{background:#f07b1d}
</style>
</head>
<body>
<header class="site-header">
  <div class="brand"><span class="brand-mark"></span><span class="brand-name">Pruett Design &amp; Millwork</span></div>
  <div class="call"><div class="call-label">CALL US NOW</div><div class="call-number">623-555-0148</div></div>
  <nav class="main-nav">
    <a href="#">HOME</a><a href="#" class="current">ABOUT US</a><a href="#">MILLWORK PROJECTS</a><a href="#">HOUSE DESIGNS</a><a href="#">CONTACT US</a>
  </nav>
</header>

<div class="hero" role="img" aria-label="Modern white house with pool and lawn"></div>

<aside class="sidebar">
  <section class="side-box">
    <h2 class="side-title red">SubMenu Links</h2>
    <ul class="submenu">
      <li>Futur etudiant</li><li>Etudiant octuel</li><li>Enterprise</li><li>Employeur</li><li>Postulant</li><li>Medias</li><li>Partenaires</li>
    </ul>
  </section>
  <section class="side-box">
    <h2 class="side-title dark">Recent Posts</h2>
    <ul class="posts">
      <li>Morbi diam mauris viverra in gravida eu mattis</li>
      <li>In ante Morbi eget arcu Morbi porta libero id</li>
      <li>Ullamcorper nonummy nibh ligula pulvinar metus</li>
      <li>Eget consv et scelerisque mi tortor at ipsum</li>
    </ul>
  </section>
</aside>

<main class="content">
  <h1>About Our Company</h1>
  <p>Aliquam nec erat at purus cursus interdum. Vestibulum ligula augue, bibendum accumsan, vestibulum ut, commodo a, mi. Morbi ornare gravida elit. Integer congue, augue et malesuada iaculis, ipsum dui aliquet felis, at cursus magna nisl nec</p>
  <p>Mauris vel lacus vitae felis vestibulum volutpat. Etiam est nunc, venenatis in, tristique eu, imperdiet ac, nisl. Cum sociis natoque penati-bus et magnis dis parturient montes, nascetur ridiculus mus. In iaculis facilisis massa.</p>
  <p>Etiam eu urna. Sed porta. Suspendisse quam leo, molestie sed, luctus quis, feugiat in, pede. Fusce tellus. Sed metus augue, convallis et, vehicula ut, pulvinar eu, ante. Integer orci tellus,</p>
  <p class="gap">tristique vitae, consequat nec, porta vel, lectus. Nulla sit amet diam. Duis non nunc. Nulla rhoncus dictum metus. Curabitur tristique mi condimentum orci. Phasellus pellentesque aliquam enim. Proin dui lectus, cursus eu, mattis laoreet, viverra sit amet, quam. Curabitur vel dolor ultrices ipsum dictum tristique. Praesent vitae lacus. Ut velit enim, vestibulum non, fermentum nec, hendrerit quis, leo. Pellen-tesque rutrum malesuada neque.</p>
  <div class="gallery">
    <div class="thumb plan" role="img" aria-label="Blue house blueprint drawing"></div>
    <div class="thumb night" role="img" aria-label="Modern building lit at dusk by the water"></div>
  </div>
  <p>Aliquam nec erat at purus cursus interdum. Vestibulum ligula augue, bibendum accumsan, vestibulum ut, commodo a, mi. Morbi ornare gravida elit. Integer congue, augue et malesuada iaculis, ipsum dui aliquet felis, at cursus magna nisl nec</p>
  <p>Mauris vel lacus vitae felis vestibulum volutpat. Etiam est nunc, venenatis in, tristique eu, imperdiet ac, nisl. Cum sociis natoque penati-bus et magnis dis parturient montes, nascetur ridiculus mus. In iaculis facilisis massa.</p>
  <p>Etiam eu urna. Sed porta. Suspendisse quam leo, molestie sed, luctus quis, feugiat in, pede. Fusce tellus. Sed metus augue, convallis et, vehicula ut, pulvinar eu, ante. Integer orci tellus,</p>
  <p class="gap">tristique vitae, consequat nec, porta vel, lectus. Nulla sit amet diam. Duis non nunc. Nulla rhoncus dictum metus. Curabitur tristique mi condimentum orci. Phasellus pellentesque aliquam enim. Proin dui lectus, cursus eu, mattis laoreet, viverra sit amet, quam. Curabitur vel dolor ultrices ipsum dictum tristique. Praesent vitae lacus. Ut velit enim, vestibulum non, fermentum nec, hendrerit quis, leo. Pellen-tesque rutrum malesuada neque.</p>
</main>

<footer class="site-footer">
  <div class="footer-brand"><span class="brand-mark"></span><span class="brand-name">Pruett Design &amp; Millwork</span></div>
  <nav class="footer-nav">Home<span>|</span>About us<span>|</span>Millwork projects<span>|</span>House designs<span>|</span>Contact us</nav>
  <div class="copyright">Copyright © 2013 Company Name.&nbsp; All right reserved</div>
  <div class="social"><i class="s1"></i><i class="s2"></i><i class="s3"></i><i class="s4"></i></div>
</footer>
</body>
</html>
```